WEEKLY INFORMATIONAL GARDENING NEWSLETTER

New Weekly Email Newsletter needs a banner that reflects company logos, author photo for new Email Campaign using Mail Chimp.

I have attached author photo, as well as our company logos.

The tile of Newsletter should read Tom's Garden Notes. Company colors are black, lime green, white for SodCraft. Colors for sister company, Verdant Mist are black, blue, green as depicted in logos attached. Logos should be on black background. I have attached a photo of the template we are considering using in mail chimp for your reference.

If you have any questions or need additional photos please let me know. Look forward to seeing your designs!

Target Market(s)

Current Clients, potential leads

Industry/Entity Type

Landscape Gardening

Font styles to use
Serif

Colors
9bcb3c
000000

Requirements
Must have
• Colors chosen below, cut out of photo, more life like than picture frame.
• Both company logos
Nice to have
• logos incorporated, as well as author photo.
Should not have
• Sales Pitch, should not have photo in frame.

```html
<!DOCTYPE html>
<html lang="en">
<head>
<meta charset="utf-8">
<title>Tom's Garden Notes — Newsletter Banner</title>
<link rel="stylesheet" href="https://fonts.googleapis.com/css2?family=Tinos:wght@400;700&display=swap">
<style>
  :root {
    --ink: #000000;
    --paper: #ffffff;
    --paper-shade: #e6e6e6;
    --charcoal: #2b2b2b;
    --mist-blue: #2a8fd0;
    --lime: #9bcb3c;
    --ghost: #161616;
    --title: #f4f4f4;
  }
  * { margin: 0; padding: 0; box-sizing: border-box; }
  html, body { width: 1200px; height: 400px; overflow: hidden; background: var(--ink); }
  .banner {
    position: relative;
    width: 1200px;
    height: 400px;
    overflow: hidden;
    font-family: "Tinos", "Times New Roman", serif;
    background: var(--ink);
  }
  .logo-bar {
    position: absolute;
    left: 0; top: 0;
    width: 1200px; height: 156px;
    background: linear-gradient(90deg, var(--paper) 0%, var(--paper) 60%, var(--paper-shade) 100%);
  }
  .brand-main {
    position: absolute;
    left: 80px; top: 22px;
    display: flex; align-items: flex-start; gap: 16px;
  }
  .brand-main .mark {
    width: 44px; height: 44px;
    margin-top: 26px;
    background: var(--charcoal);
  }
  .brand-main .name {
    font-size: 46px; font-weight: 400;
    letter-spacing: 2px; color: var(--charcoal);
    line-height: 0.95;
  }
  .brand-main .tagline {
    display: block;
    margin-top: 10px;
    font-size: 10px; letter-spacing: 1.5px;
    white-space: nowrap;
  }
  .brand-sister {
    position: absolute;
    left: 412px; top: 28px;
    display: flex; align-items: center; gap: 20px;
  }
  .brand-sister .mark {
    width: 76px; height: 76px; border-radius: 50%;
    background: var(--mist-blue);
    flex: none;
  }
  .brand-sister .name {
    font-size: 40px; font-weight: 400;
    color: var(--mist-blue); line-height: 1; letter-spacing: 0.5px;
    white-space: nowrap;
  }
  .brand-sister .tagline {
    margin-top: 8px;
    font-size: 16px; letter-spacing: 0.8px;
    color: var(--lime); white-space: nowrap;
  }
  .ghost-name {
    position: absolute;
    left: 120px; top: 166px;
    font-size: 66px; font-weight: 400; letter-spacing: 6px;
    color: var(--ghost); white-space: nowrap;
  }
  .newsletter-title {
    position: absolute;
    left: 36px; top: 314px;
    font-size: 52px; font-weight: 400; letter-spacing: 4px;
    color: var(--title); white-space: nowrap;
  }
  .author-photo {
    position: absolute;
    left: 910px; top: 44px;
    width: 290px; height: 356px;
    border-radius: 140px 0 0 0;
    background: radial-gradient(ellipse at 50% 48%, #c98a62 0%, #8a5a3c 32%, #2a1c14 62%, #0b0b0b 85%);
  }
</style>
</head>
<body>
  <div class="banner">
    <header class="logo-bar">
      <div class="brand-main">
        <span class="mark"></span>
        <div class="name">SOD<br>CRAFT
          <span class="tagline">GARDEN DESIGN BY TOM HARLOW</span>
        </div>
      </div>
      <div class="brand-sister">
        <span class="mark"></span>
        <div>
          <div class="name">VERDANT MIST</div>
          <div class="tagline">A DIVISION OF SODCRAFT</div>
        </div>
      </div>
    </header>

    <div class="ghost-name" aria-hidden="true">SODCRAFT</div>

    <h1 class="newsletter-title">Tom's Garden Notes</h1>

    <div class="author-photo" role="img" aria-label="Cut-out portrait of the smiling author in a black cap and black shirt"></div>
  </div>
</body>
</html>
```